Memoir author looking for book cover design

Title:
"Tides, Thorns and Twilight"

Subtitle:
"The Journey to Reach my Brother, Vanished on the Glacier"

My book is about the 18-month-long search and grieving process after my husband went missing from a hiking accident.
See "notesbeyondthequietfjord.example" for background

(An "ampersand" may look best, but I'm unable to enter it in this format)

Reason: Having difficulty finishing up, in part due to time difference. Don't want designers to have to work in the middle of the night!

```html
<!DOCTYPE html>
<html lang="en">
<head>
<meta charset="utf-8">
<title>Tides, Thorns and Twilight — Book Cover</title>
<link rel="stylesheet" href="https://fonts.googleapis.com/css2?family=Source+Sans+3:wght@400&family=Sorts+Mill+Goudy&family=Cutive+Mono&display=swap">
<style>
  :root {
    --ink: #0a0a0a;
    --paper: #ffffff;
    --accent: #e3231b;
    --mist-light: #d9d9d9;
    --mist-mid: #9a9a9a;
    --mist-dark: #4a4a4a;
    --rule: #cfcfcf;
  }
  * { margin: 0; padding: 0; box-sizing: border-box; }
  html, body { width: 986px; height: 1200px; overflow: hidden; background: var(--ink); }
  .cover {
    position: relative;
    width: 986px;
    height: 1200px;
    background: var(--ink);
    color: var(--paper);
    overflow: hidden;
  }

  /* Spine */
  .spine {
    position: absolute;
    left: 0; top: 0;
    width: 136px; height: 1200px;
    background: var(--ink);
  }
  .spine-line {
    position: absolute;
    white-space: nowrap;
    font-family: "Source Sans 3", "Myriad Pro", sans-serif;
    font-weight: 400;
    color: var(--paper);
    transform: translate(-50%, -50%) rotate(-90deg);
    line-height: 1;
  }
  .spine-title { left: 40px; top: 598px; font-size: 25px; }
  .spine-subtitle { left: 88px; top: 598px; font-size: 23px; }
  .spine-rule {
    position: absolute;
    left: 20px; top: 1082px;
    width: 102px; height: 1px;
    background: var(--rule);
  }
  .spine-author {
    position: absolute;
    left: 18px; top: 1086px;
    font-family: "Cutive Mono", "Courier New", monospace;
    font-size: 30px;
    line-height: 1.1;
    letter-spacing: 1px;
    color: var(--paper);
  }

  /* Front */
  .cover-art {
    position: absolute;
    left: 136px; top: 0;
    width: 850px; height: 512px;
    background:
      linear-gradient(to bottom, rgba(10,10,10,0) 55%, rgba(10,10,10,0.85) 88%, var(--ink) 100%),
      radial-gradient(ellipse at 70% 35%, var(--mist-light) 0%, var(--mist-mid) 45%, var(--mist-dark) 100%);
  }
  .book-title {
    font-weight: 400;
    font-size: inherit;
  }
  .title-line {
    position: absolute;
    font-family: "Source Sans 3", "Myriad Pro", sans-serif;
    font-weight: 400;
    line-height: 1;
    white-space: nowrap;
    color: var(--paper);
  }
  .title-top { left: 210px; top: 565px; font-size: 134px; letter-spacing: -2px; }
  .title-bottom { left: 318px; top: 723px; font-size: 150px; letter-spacing: -2px; }
  .title-joiner {
    position: absolute;
    left: 266px; top: 786px;
    font-family: "Source Sans 3", "Myriad Pro", sans-serif;
    font-weight: 400;
    font-size: 94px;
    line-height: 1;
    color: var(--accent);
    transform: translate(-50%, -50%) rotate(-90deg);
  }
  .rule {
    position: absolute;
    height: 1px;
    background: var(--rule);
  }
  .rule-upper { left: 242px; top: 886px; width: 636px; }
  .rule-lower { left: 614px; top: 1046px; width: 272px; }
  .subtitle {
    position: absolute;
    left: 238px; width: 648px;
    font-family: "Sorts Mill Goudy", "Goudy Old Style", serif;
    color: var(--paper);
    line-height: 1;
    white-space: nowrap;
  }
  .subtitle-first { top: 906px; font-size: 43px; }
  .subtitle-second { top: 978px; font-size: 43px; letter-spacing: 5.5px; }
  .byline {
    position: absolute;
    right: 90px; top: 1066px;
    font-family: "Cutive Mono", "Courier New", monospace;
    font-size: 32px;
    letter-spacing: 1px;
    color: var(--paper);
    line-height: 1;
  }
</style>
</head>
<body>
<div class="cover">
  <aside class="spine">
    <div class="spine-line spine-title">Tides, Thorns and Twilight</div>
    <div class="spine-line spine-subtitle">The Journey to Reach my Brother, Vanished on the Glacier</div>
    <div class="spine-rule"></div>
    <div class="spine-author">Nora<br>Hayes</div>
  </aside>

  <main class="front">
    <div class="cover-art" role="img" aria-label="Cover artwork area in misty greys fading into the black lower half"></div>

    <h1 class="book-title">
      <span class="title-line title-top">Tides,thorns</span>
      <span class="title-joiner">and</span>
      <span class="title-line title-bottom">Twilight</span>
    </h1>

    <div class="rule rule-upper"></div>
    <p class="subtitle subtitle-first">The Journey to Reach my Brother</p>
    <p class="subtitle subtitle-second">Vanished on the Glacier</p>
    <div class="rule rule-lower"></div>

    <p class="byline">By Nora Hayes</p>
  </main>
</div>
</body>
</html>
```